Web Developer Needs a Business Card Design

I need a personal business card design that represents me as a web developer for potential employers. I would like the background to be a dark color on the front for contrast with my logo and name. The back will have all my information along with a smaller version of the logo. I want something with a modern look and feel, not too conservative. This will be used for potential employers and freelance work.

Industry/Entity Type

Business

Contact Information for Business Card

Front should have my logo and name. The back should have all my personal information which would include: name: Tom Varnuch, phone: 570-614-9083, email: tomvarnuch@mailnest.example, website url: www.tomvarnuch.example, logo, web developer.

Font styles to use
Sans Serif

Requirements
Must have
• Must include my logo. The color palette base color will be the logo color.

```html
<!DOCTYPE html>
<html lang="en">
<head>
<meta charset="utf-8">
<title>Tom Varnuch – Business Card</title>
<link href="https://fonts.googleapis.com/css2?family=Lato:wght@400;700&display=swap" rel="stylesheet">
<style>
  :root {
    --teal: #7fd3c4;
    --teal-text: #5fbfae;
    --teal-dark: #3a9888;
    --teal-darker: #2a7a6d;
    --paper: #f6f7f5;
    --backdrop: #e7e8e6;
  }
  * { margin: 0; padding: 0; box-sizing: border-box; }
  html, body { width: 1200px; height: 780px; overflow: hidden; }
  body {
    background: var(--backdrop);
    font-family: "Lato", "Helvetica Neue", Arial, sans-serif;
    position: relative;
  }
  .card {
    position: absolute;
    width: 540px;
    height: 310px;
    top: 235px;
    border-radius: 3px;
    overflow: hidden;
    box-shadow: 0 4px 14px rgba(0,0,0,0.14);
  }
  .card--back  { left: 40px; background: var(--paper); }
  .card--front { left: 620px; background: linear-gradient(135deg, var(--teal-dark) 0%, var(--teal-darker) 100%); }

  .band { position: absolute; left: 0; width: 100%; }
  .band-rule { height: 2px; }

  .card--back .band-main { top: 62px; height: 70px; background: var(--teal); }
  .card--back .band-rule { background: var(--teal); }
  .card--back .band-rule--top { top: 52px; }
  .card--back .band-rule--bottom { top: 140px; }

  .card--front .band-main { top: 122px; height: 82px; background: var(--paper); }
  .card--front .band-rule { background: var(--paper); }
  .card--front .band-rule--top { top: 111px; }
  .card--front .band-rule--bottom { top: 213px; }

  .brand-mark {
    position: absolute;
    border-radius: 50%;
    background: var(--paper);
    display: flex;
    align-items: center;
    justify-content: center;
    font-weight: 700;
    letter-spacing: 0.5px;
    box-shadow: 0 0 0 5px var(--paper);
  }
  .card--back .brand-mark {
    width: 104px; height: 104px; left: 118px; top: 45px;
    border: 6px solid var(--teal);
    color: var(--teal-text);
    font-size: 15px;
  }
  .card--front .brand-mark {
    width: 120px; height: 120px; left: 210px; top: 103px;
    border: 6px solid var(--teal-dark);
    color: var(--teal-dark);
    font-size: 17px;
  }

  .contact {
    position: absolute;
    left: 150px;
    top: 166px;
    color: var(--teal-text);
  }
  .contact__name { font-size: 23px; font-weight: 700; text-transform: uppercase; letter-spacing: 0.5px; line-height: 1; }
  .contact__title { font-size: 14px; margin-top: 4px; }
  .contact__details { list-style: none; margin-top: 16px; font-size: 14px; line-height: 1.4; }

  .front-name {
    position: absolute;
    left: 0; width: 100%;
    top: 58px;
    text-align: center;
    color: var(--paper);
    font-size: 23px;
    font-weight: 700;
    text-transform: uppercase;
    letter-spacing: 0.5px;
  }
</style>
</head>
<body>
  <section class="card card--back" aria-label="Card back">
    <div class="band band-rule band-rule--top"></div>
    <div class="band band-main"></div>
    <div class="band band-rule band-rule--bottom"></div>
    <div class="brand-mark">Varnuch</div>
    <div class="contact">
      <p class="contact__name">Tom Varnuch</p>
      <p class="contact__title">Web Developer</p>
      <ul class="contact__details">
        <li>570-614-9083</li>
        <li>tomvarnuch@mailnest.example</li>
        <li>www.tomvarnuch.example</li>
      </ul>
    </div>
  </section>

  <section class="card card--front" aria-label="Card front">
    <p class="front-name">Tom Varnuch</p>
    <div class="band band-rule band-rule--top"></div>
    <div class="band band-main"></div>
    <div class="band band-rule band-rule--bottom"></div>
    <div class="brand-mark">Varnuch</div>
  </section>
</body>
</html>
```